Tolvane BrandWorks Corporate Site

Design a site to replace www.tolvanebrandworks.com, built for/within net harbor and incorporate numerous corporate assets and lines of business (www.pulsarstageworksinc.com, www.summitoutingpros.com, www.zapsnapkiosk.com, www.nibblecrate.com, www.strumbleorama.com) as well as our consulting and artist management work.

Target Market(s)

businesses, non profits, talent (performing artists)

Industry/Entity Type

Business

Coding

Coded - Design and coding required

Number of Pages Required

5+ page

Colors
0655a3
ffc214

Requirements
Must have
• social media visibility, multi-media

```html
<!DOCTYPE html>
<html lang="en">
<head>
<meta charset="utf-8">
<title>Tolvane BrandWorks</title>
<link href="https://fonts.googleapis.com/css2?family=Libre+Baskerville:wght@400;700&family=PT+Serif:wght@400;700&family=Open+Sans:wght@400;600&display=swap" rel="stylesheet">
<style>
:root{
  --blue:#0c3f7a;
  --brand-blue:#0655a3;
  --gold:#e2a50e;
  --gold-bright:#ffc214;
  --ink:#333;
  --muted:#555;
  --band:#efefef;
  --footer:#4a4a4a;
  --footer-text:#c8c8c8;
  --bar:#3a3a3a;
  --white:#fff;
}
*{margin:0;padding:0;box-sizing:border-box}
html,body{width:693px;height:1200px;overflow:hidden;background:var(--white)}
body{position:relative;font-family:'Open Sans',sans-serif;color:var(--ink)}
.abs{position:absolute}
/* header */
.site-header{left:0;top:0;width:693px;height:69px;background:var(--white);box-shadow:0 1px 4px rgba(0,0,0,.15);z-index:2}
.logo{left:58px;top:18px}
.logo-name{font-family:'Libre Baskerville',serif;font-size:19px;color:var(--blue);letter-spacing:-.3px;line-height:1;white-space:nowrap}
.logo-tag{font-family:'Libre Baskerville',serif;font-size:6.3px;color:var(--muted);letter-spacing:.4px;margin-top:3px;border-top:1px solid #9aa;padding-top:2px;white-space:nowrap}
.main-nav{left:0;top:32px;width:693px;height:16px;font-family:'PT Serif',serif;font-size:9px;color:#222}
.main-nav span{position:absolute;top:0;white-space:nowrap;line-height:11px}
.main-nav .active{color:var(--brand-blue);border-bottom:1px solid var(--brand-blue);padding-bottom:4px}
.search-icon{left:628px;top:34px}
/* hero */
.hero{left:0;top:70px;width:693px;height:296px;background:linear-gradient(100deg,#c9d3dc 0%,#e9eef2 35%,#f4f6f8 55%,#b9c4cf 80%,#d8dee3 100%)}
.hero-arrow{left:24px;top:205px}
.hero-caption{left:287px;top:245px;width:349px;height:45px;background:rgba(70,70,70,.85);color:var(--white);font-family:'PT Serif',serif;font-weight:700;font-size:13px;letter-spacing:.6px;display:flex;align-items:center;justify-content:center;white-space:nowrap}
/* welcome */
.section-title{width:693px;text-align:center;font-family:'Libre Baskerville',serif;font-weight:700;font-size:15.5px;white-space:nowrap}
.welcome-title{top:393px}
.welcome-title .lead{color:var(--gold)}
.welcome-title .name{color:var(--blue)}
.welcome-text{left:82px;top:422px;width:530px;text-align:center;font-size:6.6px;line-height:13px;color:var(--muted)}
.service-card{top:478px;width:185px;height:128px;border:1px solid #e4e4e4;padding:3px;background:var(--white)}
.service-photo{width:100%;height:100%;position:relative}
.service-label{position:absolute;left:50%;bottom:18px;transform:translateX(-50%);background:var(--white);font-size:6.8px;color:#333;padding:5px 10px;white-space:nowrap}
/* blog */
.blog-band{left:0;top:643px;width:693px;height:310px;background:linear-gradient(180deg,#e2a617,#e0a10d)}
.blog-title{top:660px}
.blog-title .lead{color:var(--white)}
.blog-title .name{color:var(--blue)}
.blog-card{top:696px;width:282px;height:157px;border:3px solid var(--white)}
.blog-photo{width:100%;height:100%;position:relative}
.blog-badges{position:absolute;right:0;top:0;width:32px}
.badge{height:20px;display:flex;align-items:center;justify-content:center}
.badge.comment{background:var(--gold)}
.badge.date{background:var(--blue)}
.blog-body{position:absolute;left:15px;top:86px;width:210px;color:var(--white)}
.blog-body h3{font-size:9px;font-weight:600;margin-bottom:3px}
.blog-body p{font-size:6.5px;line-height:12.5px}
.blog-body .more{font-size:6.5px;font-weight:600;margin-top:5px;display:flex;align-items:center;gap:4px}
.view-more{left:314px;top:890px;width:69px;height:27px;border:1px solid var(--white);color:var(--white);font-size:8px;display:flex;align-items:center;justify-content:center;letter-spacing:.3px}
/* partners */
.partners{left:0;top:953px;width:693px;height:77px;background:var(--band);display:flex;justify-content:space-around;align-items:center;padding:0 40px}
.partner{display:flex;align-items:center;gap:5px;font-size:14px;font-weight:600;color:#555}
.partner i{display:block;width:13px;height:13px;border-radius:50%;background:#666}
/* footer */
.site-footer{left:0;top:1030px;width:693px;height:136px;background:var(--footer);color:var(--footer-text)}
.footer-col{top:16px}
.footer-col h4{font-size:9px;font-weight:600;color:var(--white);margin-bottom:9px}
.footer-col p,.footer-col li{font-size:6.8px;line-height:11px}
.footer-col ul{list-style:none}
.footer-col li{margin-bottom:5.3px}
.contact-line{display:flex;align-items:center;gap:8px;margin-top:6px;font-size:7px}
.newsletter-input{width:101px;height:18px;background:#6c6c6c;border:1px solid #7a7a7a;border-radius:2px;font-size:5.5px;font-style:italic;color:#ccc;padding:5px 6px;margin-top:10px}
.subscribe{margin-top:13px;width:60px;height:19px;background:var(--gold-bright);color:#3a2a00;font-size:6.8px;font-weight:600;display:flex;align-items:center;justify-content:center;border-radius:2px}
.social li{display:flex;align-items:center;gap:9px}
.social i{display:block;width:8px;height:8px;border-radius:50%;background:var(--white)}
.bottom-bar{left:0;top:1166px;width:693px;height:34px;background:var(--bar);color:#ddd;font-size:6.8px;display:flex;align-items:center;justify-content:center}
</style>
</head>
<body>

<header class="site-header abs">
  <div class="logo abs">
    <div class="logo-name">Tolvane BrandWorks</div>
    <div class="logo-tag">STRATEGIC MARKETING &amp; COMMUNICATIONS</div>
  </div>
  <nav class="main-nav abs">
    <span class="active" style="left:266px">Home</span>
    <span style="left:310px">About</span>
    <span style="left:353px">Our Services</span>
    <span style="left:422px">Clients</span>
    <span style="left:469px">News &amp; Events</span>
    <span style="left:547px">Blog</span>
    <span style="left:584px">Contact</span>
  </nav>
  <svg class="search-icon abs" width="9" height="9" viewBox="0 0 10 10"><circle cx="4" cy="4" r="3" fill="none" stroke="#e2a50e" stroke-width="1.6"/><line x1="6.2" y1="6.2" x2="9.3" y2="9.3" stroke="#e2a50e" stroke-width="1.8"/></svg>
</header>

<section class="hero abs" role="img" aria-label="Presenter at a whiteboard chart leading a meeting with colleagues in a bright office"></section>
<svg class="hero-arrow abs" width="10" height="30" viewBox="0 0 10 30"><polyline points="9,1 1,15 9,29" fill="none" stroke="#fff" stroke-width="1.3"/></svg>
<div class="hero-caption abs">COMMUNICATE , COLLABORATE , CELEBRATE</div>

<h2 class="section-title welcome-title abs"><span class="lead">WELCOME TO </span><span class="name">TOLVANEBRANDWORKS</span></h2>
<p class="welcome-text abs">Is your marketing and communications partner responsive, and flexible? &nbsp;Creative, yet practical? Do they understand your business enough to be strategic? Do they care enough to be passionate? &nbsp;Your business deserves no less. &nbsp;In fact, it deserves much more. &nbsp;Since 2000, Tolvane BrandWorks has assisted businesses of all sizes, in generating true marketplace returns on their marcom investments.</p>

<div class="service-card abs" style="left:58px">
  <div class="service-photo" role="img" aria-label="Business team standing in front of a world map" style="background:linear-gradient(180deg,#5b5b5b,#1e1e1e)">
    <span class="service-label">PUBLIC RELATIONS</span>
  </div>
</div>
<div class="service-card abs" style="left:253px">
  <div class="service-photo" role="img" aria-label="Strategy meeting around a flip chart" style="background:linear-gradient(160deg,#e8ecef,#9ba6b0 70%,#3d4650)">
    <span class="service-label">STRATEGIC MARKETING</span>
  </div>
</div>
<div class="service-card abs" style="left:450px">
  <div class="service-photo" role="img" aria-label="Diverse group of young professionals" style="background:linear-gradient(180deg,#c9dbe6,#7b6e66 60%,#2e2e36)">
    <span class="service-label">MULTICULTURAL MARKETING</span>
  </div>
</div>

<section class="blog-band abs"></section>
<h2 class="section-title blog-title abs"><span class="lead">TOLVANE </span><span class="name">BLOG</span></h2>

<article class="blog-card abs" style="left:58px">
  <div class="blog-photo" role="img" aria-label="Hand pulling a card reading success from a suit pocket" style="background:linear-gradient(120deg,#7a6a88,#3b3f7e 55%,#22266a)">
    <div class="blog-badges">
      <div class="badge comment"><svg width="9" height="8" viewBox="0 0 10 9"><ellipse cx="5" cy="4" rx="5" ry="3.6" fill="#fff"/><path d="M2 6 L1 9 L4 7z" fill="#fff"/></svg></div>
      <div class="badge date"><svg width="8" height="8" viewBox="0 0 8 8"><rect x=".5" y="1" width="7" height="6.5" fill="none" stroke="#fff"/><line x1=".5" y1="3" x2="7.5" y2="3" stroke="#fff"/></svg></div>
    </div>
    <div class="blog-body">
      <h3>FINIBUS BONORUM</h3>
      <p>Lorem Ipsum is simply dummy text of the printing and typeset-ting industry. Lorem Ipsum has been the industry's.</p>
      <div class="more">Read More <svg width="7" height="7" viewBox="0 0 8 8"><circle cx="4" cy="4" r="4" fill="#fff"/><polyline points="3,2 5,4 3,6" fill="none" stroke="#333" stroke-width="1.2"/></svg></div>
    </div>
  </div>
</article>
<article class="blog-card abs" style="left:354px">
  <div class="blog-photo" role="img" aria-label="Businessman with arms outstretched among city towers" style="background:linear-gradient(180deg,#b8c3cc,#6f7b86 55%,#3a434c)">
    <div class="blog-badges">
      <div class="badge comment"><svg width="9" height="8" viewBox="0 0 10 9"><ellipse cx="5" cy="4" rx="5" ry="3.6" fill="#fff"/><path d="M2 6 L1 9 L4 7z" fill="#fff"/></svg></div>
      <div class="badge date"><svg width="8" height="8" viewBox="0 0 8 8"><rect x=".5" y="1" width="7" height="6.5" fill="none" stroke="#fff"/><line x1=".5" y1="3" x2="7.5" y2="3" stroke="#fff"/></svg></div>
    </div>
    <div class="blog-body">
      <h3>FINIBUS BONORUM</h3>
      <p>Lorem Ipsum is simply dummy text of the printing and typeset-ting industry. Lorem Ipsum has been the industry's.</p>
      <div class="more">Read More <svg width="7" height="7" viewBox="0 0 8 8"><circle cx="4" cy="4" r="4" fill="#fff"/><polyline points="3,2 5,4 3,6" fill="none" stroke="#333" stroke-width="1.2"/></svg></div>
    </div>
  </div>
</article>
<div class="view-more abs">VIEW MORE</div>

<section class="partners abs">
  <span class="partner"><i></i>Pressbase</span>
  <span class="partner"><i></i>Jumlet</span>
  <span class="partner"><i></i>Magnolith</span>
  <span class="partner"><i></i>Dropcore</span>
  <span class="partner"><i></i>Queryline</span>
</section>

<footer class="site-footer abs">
  <div class="footer-col abs" style="left:67px">
    <h4>Contact Us</h4>
    <p>Tolvane BrandWorks Inc.<br>4120 Alder Crest Rd. * Westgate Plaza,<br>Suite 305 * Millbrook, GA 30190</p>
    <div class="contact-line"><svg width="10" height="9" viewBox="0 0 10 10"><path d="M2 1 L4 3 L3 4.5 Q4.5 6.5 6 7 L7 6 L9 8 L7.5 9.5 Q2 8 .5 2.5z" fill="none" stroke="#e2a50e" stroke-width=".9"/></svg>555.218.4470</div>
    <div class="contact-line"><svg width="11" height="8" viewBox="0 0 11 8"><rect x=".5" y=".5" width="10" height="7" fill="none" stroke="#e2a50e"/><polyline points=".5,.5 5.5,4.5 10.5,.5" fill="none" stroke="#e2a50e"/></svg>info@tolvanebrandworks.com</div>
  </div>
  <div class="footer-col abs" style="left:250px">
    <h4>Quick Links</h4>
    <ul><li>Home</li><li>About</li><li>What`s new</li><li>What we do</li><li>Contacts</li></ul>
  </div>
  <div class="footer-col abs" style="left:384px">
    <h4>Newsletter sign up</h4>
    <p>Please sign up here for &nbsp;news</p>
    <div class="newsletter-input">Email address</div>
    <div class="subscribe">SUBSCRIBE</div>
  </div>
  <div class="footer-col abs" style="left:573px">
    <h4>Follow Us</h4>
    <ul class="social"><li><i></i>Friendhall</li><li><i></i>Chirpline</li><li><i></i>Circlespace</li></ul>
  </div>
</footer>
<div class="bottom-bar abs">© 2016 Tolvane BrandWorks &nbsp;All right reserved &nbsp;Term of Use</div>

</body>
</html>
```